Plakat-Design für Dienstleister in den Bereichen Einbruchschutz, Schließsysteme und Zutrittslösungen
Zielgruppe
Seit über 58 Jahren sind wir als Familienunternehmen Brenni Riegeltechnik AG in Luzern und Zug bekannt für kompetente Dienstleistungen in den Bereichen Einbruchschutz, Schliesssysteme und Zutrittslösungen. Die Brenni Riegeltechnik AG ist einer der führenden Dienstleister für Schliesssysteme, Einbruchschutz und Tresore in der Zentralschweiz. Das Unternehmen ist seit über 58 Jahren in der Zentralschweiz verankert und beschäftigt aktuell an den beiden Standorten in Luzern und Zug 60 Mitarbeitende. In dieser Zeitspanne hat sich die Firma einen bekannten Namen für wirksame Schliesssysteme, Sicherheitslösungen für Private, Gewerbe und Industrie schaffen können – insbesondere für Unternehmungen in den Branchen Immobilien, Spitäler, Heime, Banken, Versicherungen, Öffentliche Einrichtungen, Institutionen, Behörden, Militär, Schulen, Universitäten, Sport, Kultur, Freizeit, Hotels sowie Jugendherbergen.
Plakat/Symbolik für weitere HR Marketing-Massnahmen - Führungsgrundsätze
Zielgruppe ist die bestehenden Mitarbeiter und zukünftigen Mitarbeiter. Es geht um 4 Führungsgrundsätze, welche dieses Jahr mit dem Kader und der Geschäftsleitung erarbeitet wurde, diese im Betrieb intern öffentlich aufzuzeigen und stets präsent zu haben. Aber auch für zukünftige potentielle neue Mitarbeiter soll es die Möglichkeit ergeben, offen über unsere Führungsgrundsätze zu informieren und transparent aufzuzeigen.
Aufgabenstellung
Es wurden 4 Führungsgrundsätze definiert; welche gestalterisch präsentiert werden sollen (intern - plakativ - Aufenthaltsraum, Toiletten,Treppenhaus, Deskophintergrund, Mitarbeiterbroschüre, Homepage, etc.)
-Perspektive ermöglichen
-Vertrauen & Sicherheit geben
-Miteinander wirken
-Freude erleben
Ergänzungen zu den vier Führungsgrundsätze von unserer Firma aus den Meeting siehe Anhang.
Ziel ist es, 2 Plakate zu haben: 1x alle 4 Grundsätze (Oberbegriffe) & je 1 Seite Plakat je Führungsgrundsatz mit den Ergänzungen.

```html
<!DOCTYPE html>
<html lang="de">
<head>
<meta charset="utf-8">
<title>Brenni – Eure Führungsgrundsätze</title>
<link href="https://fonts.googleapis.com/css2?family=Poppins:wght@500;600;700&display=swap" rel="stylesheet">
<style>
  :root {
    --brand-blue: #0b4a96;
    --bar-dark: #272c31;
    --panel-white: #ffffff;
    --text-dark: #2a2e34;
    --logo-blue: #1f5fb0;
    --art-light: #dfe7f1;
    --art-deep: #c9d6e8;
  }
  * { box-sizing: border-box; margin: 0; padding: 0; }
  html, body { width: 872px; height: 1200px; overflow: hidden; background: #fff; }
  body { font-family: "Poppins", sans-serif; }
  .poster {
    position: relative;
    width: 872px; height: 1200px;
    background: var(--brand-blue);
  }
  .brand-tab {
    position: absolute; left: 311px; top: 0;
    width: 250px; height: 93px;
    background: var(--panel-white);
    border-radius: 0 0 16px 16px;
    display: flex; align-items: center; justify-content: center;
  }
  .brand-name {
    display: flex; align-items: center; gap: 10px;
    font-weight: 700; font-size: 36px; letter-spacing: 1px;
    color: var(--logo-blue); line-height: 1;
  }
  .brand-dot { width: 14px; height: 14px; border-radius: 50%; background: var(--logo-blue); }
  .poster-title {
    position: absolute; top: 110px; left: 0; width: 100%;
    text-align: center; color: #fff;
    font-weight: 700; font-size: 52px; letter-spacing: 0.5px; line-height: 1.3;
  }
  .principles {
    position: absolute; left: 10px; right: 10px; top: 207px; bottom: 11px;
    display: grid; grid-template-columns: 1fr 1fr; grid-template-rows: 490px 1fr;
    gap: 4px;
  }
  .principle { background: var(--panel-white); display: flex; flex-direction: column; }
  .principle-title {
    height: 56px; background: var(--bar-dark); color: #fff;
    display: flex; align-items: center; justify-content: center;
    font-weight: 600; font-size: 22px; letter-spacing: 0.5px;
  }
  .principle-art {
    height: 206px; width: 260px; margin: 26px auto 0;
    border-radius: 12px;
    background: linear-gradient(160deg, var(--art-light) 0%, var(--art-deep) 100%);
  }
  .principle-list { list-style: none; padding: 14px 10px 0 37px; }
  .principle-list li {
    position: relative; padding-left: 28px; margin-bottom: 14px;
    font-weight: 600; font-size: 13.5px; line-height: 1.5; color: var(--text-dark);
    text-transform: uppercase;
  }
  .principle-list li::before {
    content: ""; position: absolute; left: 0; top: 5px;
    width: 10px; height: 10px; background: var(--text-dark);
  }
</style>
</head>
<body>
<div class="poster">
  <header class="brand-tab">
    <div class="brand-name"><span class="brand-dot"></span>BRENNI</div>
  </header>
  <h1 class="poster-title">EURE FÜHRUNGSGRUNDSÄTZE</h1>

  <main class="principles">
    <section class="principle">
      <h2 class="principle-title">PERSPEKTIVE</h2>
      <div class="principle-art" role="img" aria-label="Illustration: Person mit Fernrohr und Klemmbrett blickt in die Zukunft"></div>
      <ul class="principle-list">
        <li>Wir fördern die individuelle<br>Entwicklung unserer Mitarbeiter</li>
        <li>Wir vermitteln unser Wissen<br>Know-how</li>
        <li>Wir sind offen für Neues</li>
        <li>Wir setzen uns für das Wohlbe-<br>finden unserer Mitarbeiter ein</li>
      </ul>
    </section>
    <section class="principle">
      <h2 class="principle-title">VERTRAUEN</h2>
      <div class="principle-art" role="img" aria-label="Illustration: zwei Personen reichen sich auf Puzzleteilen die Hand"></div>
      <ul class="principle-list">
        <li>Wir kommunizieren offen, direkt<br>und ehrlich</li>
        <li>Wir sichern Arbeitsplätze durch<br>wirtschaftliches Arbeiten</li>
        <li>Wir fördern Eigeninitiative</li>
        <li>Wir lernen aus unseren Fehlern</li>
      </ul>
    </section>
    <section class="principle">
      <h2 class="principle-title">MITEINANDER</h2>
      <div class="principle-art" role="img" aria-label="Illustration: Team setzt gemeinsam eine Glühbirne aus Puzzleteilen zusammen"></div>
      <ul class="principle-list">
        <li>Alle wirken mit!</li>
        <li>Wir pflegen einen wertschät-<br>zenden &amp; fairen Umgang</li>
        <li>Wir unterstützen einander</li>
        <li>Herausfordernde Situationen<br>meistern wir zusammen</li>
      </ul>
    </section>
    <section class="principle">
      <h2 class="principle-title">FREUDE</h2>
      <div class="principle-art" role="img" aria-label="Illustration: feiernde Gruppe mit erhobenen Armen und Konfetti"></div>
      <ul class="principle-list">
        <li>Wir erschaffen Erfolgserlebnisse</li>
        <li>Wir feiern Erfolge</li>
        <li>Wir lassen Freiraum für Spass</li>
        <li>Zusammen lachen</li>
      </ul>
    </section>
  </main>
</div>
</body>
</html>
```